Business card for apparel company. Specializing in fishing and boating performance wear. Main company name is Marlow Pelican Company, LLC brand name for apparel is TIDEWAKE. See website www.TidewakeBayline.com I will attach some logos to consider.

```html
<!DOCTYPE html>
<html lang="en">
<head>
<meta charset="utf-8">
<title>Tidewake Business Card</title>
<link href="https://fonts.googleapis.com/css2?family=Roboto:wght@400;500;700;900&display=swap" rel="stylesheet">
<style>
  :root {
    --backdrop: #2b2c30;
    --paper: #ffffff;
    --brand-deep: #0b5fd9;
    --brand-bright: #09a8ea;
    --brand-band: #19a3e8;
    --brand-line: #1a5fd8;
    --ink-gray: #4a4a4a;
  }
  * { margin: 0; padding: 0; box-sizing: border-box; }
  html, body { width: 1200px; height: 952px; overflow: hidden; }
  body {
    background: var(--backdrop);
    font-family: "Roboto", sans-serif;
    position: relative;
  }
  .card {
    position: absolute;
    left: 250px;
    width: 700px;
    height: 400px;
    overflow: hidden;
    box-shadow: 0 8px 24px rgba(0,0,0,0.45);
  }
  .card-front { top: 56px; background: var(--paper); }
  .card-back {
    top: 496px;
    background: linear-gradient(135deg, var(--brand-deep) 0%, var(--brand-bright) 100%);
  }

  /* bottom accents */
  .accent-thin, .accent-band { position: absolute; }
  .card-front .accent-thin { left: 0; width: 300px; top: 360px; height: 2px; background: var(--brand-line); }
  .card-front .accent-band { left: 300px; right: 0; top: 356px; height: 9px; background: var(--brand-band); }
  .card-back .accent-band { left: 0; width: 300px; top: 356px; height: 9px; background: var(--brand-band); }
  .card-back .accent-thin { left: 300px; right: 0; top: 360px; height: 2px; background: #ffffff; }

  /* brand lockup */
  .brand {
    position: absolute;
    display: flex;
    align-items: center;
    gap: 12px;
    font-weight: 900;
    letter-spacing: 1px;
  }
  .brand-dot { width: 22px; height: 22px; border-radius: 50%; flex: none; }
  .card-front .brand { left: 48px; top: 168px; font-size: 44px; color: var(--brand-line); }
  .card-front .brand-dot { background: var(--brand-line); }
  .card-back .brand { left: 50%; top: 50%; transform: translate(-50%, -60%); font-size: 64px; color: #ffffff; }
  .card-back .brand-dot { background: #ffffff; width: 30px; height: 30px; }

  /* contact block */
  .contact { position: absolute; left: 400px; top: 74px; width: 290px; }
  .person-name { font-size: 25px; font-weight: 700; color: var(--brand-line); }
  .person-title { font-size: 14px; color: var(--ink-gray); margin-top: 4px; }
  .title-rule { width: 70px; height: 2px; background: var(--brand-line); margin: 8px 0 14px; }
  .contact-row { display: flex; align-items: flex-start; gap: 10px; margin-bottom: 8px; font-size: 14px; color: var(--ink-gray); line-height: 1.35; }
  .contact-icon { width: 18px; height: 18px; flex: none; margin-top: 1px; }
</style>
</head>
<body>
  <section class="card card-front">
    <div class="brand"><span class="brand-dot"></span>TIDEWAKE</div>

    <div class="contact">
      <div class="person-name">Marlow Pelican</div>
      <div class="person-title">CEO/Manger</div>
      <div class="title-rule"></div>

      <div class="contact-row">
        <svg class="contact-icon" viewBox="0 0 18 18"><rect width="18" height="18" rx="3" fill="#19a3e8"/><path d="M9 3.5a3.5 3.5 0 0 0-3.5 3.5C5.5 10 9 14.5 9 14.5S12.5 10 12.5 7A3.5 3.5 0 0 0 9 3.5z" fill="#fff"/><circle cx="9" cy="7" r="1.3" fill="#19a3e8"/></svg>
        <span>P.O. Box 318 Harbor Key<br>Florida 34710</span>
      </div>
      <div class="contact-row">
        <svg class="contact-icon" viewBox="0 0 18 18"><rect width="18" height="18" rx="3" fill="#19a3e8"/><path d="M5.5 4.5l2 0 1 2.5-1.3 1c.6 1.3 1.5 2.2 2.8 2.8l1-1.3 2.5 1v2c0 .5-.5 1-1 1C8 13.5 4.5 10 4.5 5.5c0-.5.5-1 1-1z" fill="#fff"/></svg>
        <span>401-555-0182</span>
      </div>
      <div class="contact-row">
        <svg class="contact-icon" viewBox="0 0 18 18"><rect width="18" height="18" rx="3" fill="#19a3e8"/><rect x="4" y="5.5" width="10" height="7" fill="none" stroke="#fff" stroke-width="1.3"/><path d="M4 5.5l5 4 5-4" fill="none" stroke="#fff" stroke-width="1.3"/></svg>
        <span>info@MarlowPelicanCo.com</span>
      </div>
      <div class="contact-row">
        <svg class="contact-icon" viewBox="0 0 18 18"><rect width="18" height="18" rx="3" fill="#19a3e8"/><path d="M4 9.5l10-5-4 10-1.3-3.7z" fill="#fff"/></svg>
        <span>www.TidewakeBayline.com</span>
      </div>
    </div>

    <div class="accent-thin"></div>
    <div class="accent-band"></div>
  </section>

  <section class="card card-back">
    <div class="brand"><span class="brand-dot"></span>TIDEWAKE</div>
    <div class="accent-band"></div>
    <div class="accent-thin"></div>
  </section>
</body>
</html>
```